MYLAR BAG FOR BLOOMA

Ive included a template for the design provided by the printer.

FRONT :
I'd like to match the box , i have a screenshot. I used an app to create it and the box printer somehow applied it. The app tells me the fonts, let me know if you would like the font names.

BACK SIDE :

DIRECTIONS FOR USE : THC TOLERANCE MAY VARY FROM PERSON TO PERSON. THE ACCEPTED RECOMMENDATION FOR A NEW USER IS 10 MG THC. REFERENCE THE AFFIXED TRALVO TAG FOR ACCURATE DOSAGE INFORMATION .

INGREDIENTS : RICE, SUGAR, THC EXTRACT, COCONUT OIL, ARTIFICIAL FLAVOR & COLOR, SALT, MALT SYRUP

ALLERGEN WARNING : CONTAINS COCONUT.
MADE IN A FACULTY THAT HANDLES PEANUTS AND OTHER TREE NUTS.

THE ACTUAL VALUE OF REPORTED CANNABINOIDS MAY VARY FROM THE REPORTED VALUE BY +/-10 %

ACTIVATION TIME :10-60 MIN

WARNING : FOR USE BY INDIVIDUALS 21 YRS OF AGE OR OLDER OR BY REGISTERED QUALIFYING PATIENTS ONLY. IT IS ILLEGAL TO DRIVE A MOTOR VEHICLE WHILE UNDER THE INFLUENCE OF MARIJUANA.

KEEP OUT OF REACH OF CHILDREN.

HARBORVALE SAFETY LINE CENTER
1 800 555 0147

WARNING : USE BY PREGNANT OR BREASTFEEDING WOMEN OR BY WOMEN WHO PLAN TO BECOME
PREGNANT MAY RESULT IN FETAL INJURY, PRETERM BIRTH, LOW BIRTHWEIGHT, OR DEVELOPMENTAL
PROBLEMS FOR THE CHILD.

MADE IN A MARIJUANA FACILITY

MADE & DISTRIBUTED BY MARLOWE'S TWIG COMPANY
LICENSE # BQ K 004736
(LOGO)
www.FENWILLOWS.INFO

• CMKY colors

```html
<!DOCTYPE html>
<html lang="en">
<head>
<meta charset="utf-8">
<title>Blooma Mylar Bag – Dieline</title>
<link href="https://fonts.googleapis.com/css2?family=Titan+One&family=Montserrat:wght@400;600;700&family=EB+Garamond&display=swap" rel="stylesheet">
<style>
  :root{
    --bag-pink:#ebb2cf;
    --paper:#ffffff;
    --ink-white:#ffffff;
    --cream:#f8f3b5;
    --dieline:#1a9b4b;
    --seal-grey:#8e6f80;
    --dim-ink:#333333;
  }
  html,body{margin:0;padding:0;width:667px;height:1200px;overflow:hidden;background:var(--paper);}
  .canvas{position:relative;width:667px;height:1200px;overflow:hidden;background:var(--paper);}
  .sheet{position:absolute;left:0;top:7px;width:1440px;height:2560px;transform:scale(0.4632);transform-origin:0 0;}
  .abs{position:absolute;}
  .dim{font-family:"EB Garamond",serif;color:var(--dim-ink);font-size:24px;}
  .dim-small{font-family:"EB Garamond",serif;color:var(--dim-ink);font-size:11px;transform:rotate(-90deg);transform-origin:center;}
  .center-line{left:406px;width:590px;text-align:center;}
  .display{font-family:"Titan One",sans-serif;line-height:1;}
  .adult-use{top:378px;left:560px;width:290px;text-align:center;font-size:36px;color:var(--ink-white);letter-spacing:2px;}
  .thc{top:452px;font-size:74px;color:var(--ink-white);letter-spacing:3px;}
  .cereal{top:520px;font-size:74px;color:var(--cream);letter-spacing:3px;}
  .frosted{top:624px;font-size:92px;color:var(--bag-pink);-webkit-text-stroke:5px var(--ink-white);letter-spacing:4px;}
  .strawberry{top:716px;font-size:58px;color:var(--ink-white);letter-spacing:5px;}
  .flavor-name{top:770px;font-size:58px;color:var(--ink-white);letter-spacing:5px;}
  .tagline{top:866px;font-family:"Montserrat",sans-serif;font-weight:700;font-size:21px;line-height:27px;letter-spacing:6px;color:var(--ink-white);}
  .brand-name{top:952px;font-size:64px;line-height:66px;color:var(--cream);letter-spacing:2px;}
  .front-warning{top:1133px;font-family:"Montserrat",sans-serif;font-weight:700;font-size:22px;letter-spacing:2px;color:var(--ink-white);}
  .back-copy{font-family:"Montserrat",sans-serif;color:var(--ink-white);font-size:11.5px;line-height:14.5px;text-transform:uppercase;}
  .back-copy b{font-weight:700;}
  .back-copy.large{font-size:14.5px;line-height:18px;}
  .pregnancy-box{left:467px;top:1970px;width:468px;height:85px;border:2px solid var(--ink-white);border-radius:8px;box-sizing:border-box;padding-top:11px;text-align:center;}
  .seal-slot{width:70px;height:70px;background:var(--seal-grey);opacity:.35;}
</style>
</head>
<body>
<div class="canvas">
  <div class="sheet">
    <svg class="abs" style="left:0;top:0" width="1440" height="2560" viewBox="0 0 1440 2560" aria-hidden="true">
      <rect x="406" y="169" width="590" height="2273" fill="var(--bag-pink)"/>
      <g fill="none" stroke="var(--dieline)">
        <rect x="406" y="169" width="590" height="2273" stroke-width="3"/>
        <line x1="406" y1="271" x2="996" y2="271" stroke-width="1.5"/>
        <line x1="406" y1="279" x2="996" y2="279" stroke-width="1.5"/>
        <line x1="406" y1="1213" x2="996" y2="1213" stroke-width="3"/>
        <line x1="406" y1="1397" x2="996" y2="1397" stroke-width="3"/>
        <line x1="406" y1="2333" x2="996" y2="2333" stroke-width="1.5"/>
        <line x1="406" y1="2341" x2="996" y2="2341" stroke-width="1.5"/>
        <g stroke-width="2" stroke-dasharray="14 9">
          <line x1="435" y1="180" x2="435" y2="298"/>
          <line x1="967" y1="180" x2="967" y2="298"/>
          <line x1="406" y1="252" x2="996" y2="252"/>
          <rect x="435" y="298" width="532" height="887"/>
          <rect x="435" y="1243" width="532" height="125"/>
          <rect x="435" y="1426" width="532" height="887"/>
          <line x1="406" y1="2358" x2="996" y2="2358"/>
          <line x1="435" y1="2313" x2="435" y2="2432"/>
          <line x1="967" y1="2313" x2="967" y2="2432"/>
        </g>
        <g stroke-width="1">
          <polyline points="408,193 414,197 408,201"/>
          <polyline points="994,193 988,197 994,201"/>
          <polyline points="408,2409 414,2413 408,2417"/>
          <polyline points="994,2409 988,2413 994,2417"/>
        </g>
        <g stroke-width="2.5">
          <line x1="366" y1="169" x2="366" y2="298"/>
          <line x1="360" y1="169" x2="372" y2="169"/>
          <line x1="360" y1="298" x2="372" y2="298"/>
          <line x1="397" y1="169" x2="397" y2="197"/>
          <line x1="392" y1="169" x2="402" y2="169"/>
          <line x1="392" y1="197" x2="402" y2="197"/>
          <line x1="397" y1="252" x2="397" y2="298"/>
          <line x1="392" y1="252" x2="402" y2="252"/>
          <line x1="392" y1="298" x2="402" y2="298"/>
        </g>
      </g>
    </svg>

    <div class="abs seal-slot" style="left:846px;top:345px" role="img" aria-label="Space for the required regulatory product symbol"></div>
    <div class="abs seal-slot" style="left:666px;top:2210px" role="img" aria-label="Space for the required regulatory product symbol"></div>

    <div class="abs dim" style="left:640px;top:127px;width:146px;text-align:center">206mm</div>
    <div class="abs dim" style="left:1007px;top:577px">365mm</div>
    <div class="abs dim" style="left:1007px;top:1303px">64mm</div>
    <div class="abs dim" style="left:1007px;top:1888px">365mm</div>
    <div class="abs dim" style="left:640px;top:1186px;width:132px;text-align:center">10mm</div>
    <div class="abs dim-small" style="left:332px;top:222px;width:36px;text-align:center">45mm</div>
    <div class="abs dim-small" style="left:368px;top:177px;width:36px;text-align:center">10mm</div>
    <div class="abs dim-small" style="left:372px;top:267px;width:36px;text-align:center">16mm</div>

    <section class="front-panel">
      <div class="abs display adult-use">ADULT - USE</div>
      <div class="abs display center-line thc">THC</div>
      <div class="abs display center-line cereal">CEREAL</div>
      <div class="abs display center-line frosted">FROSTED</div>
      <div class="abs display center-line strawberry">STRAWBERRY</div>
      <div class="abs display center-line flavor-name">BLOOMA</div>
      <div class="abs center-line tagline">FROSTED STRAWBERRY<br>CEREAL ENHANCED WITH THC</div>
      <div class="abs display center-line brand-name">FEN<br>WILLOWS</div>
      <div class="abs center-line front-warning">KEEP OUT OF REACH OF CHILDREN</div>
    </section>

    <section class="back-panel">
      <div class="abs center-line back-copy" style="top:1472px"><b>Directions for use :</b><br>THC tolerance may vary from person to person. The accepted<br>recommendation for a new user is 10 mg THC. Reference the<br>affixed TRALVO tag for accurate dosage information .</div>
      <div class="abs center-line back-copy" style="top:1557px"><b>Ingredients :</b><br>Rice, sugar, THC extract, coconut oil, artificial flavor &amp; color,<br>salt, malt syrup</div>
      <div class="abs center-line back-copy" style="top:1629px"><b>Allergen warning :</b><br>Contains coconut. Made in a faculty that handles peanuts and<br>other tree nuts.</div>
      <div class="abs center-line back-copy" style="top:1687px">The actual value of reported cannabinoids may vary from the<br>reported value by +/-10 %</div>
      <div class="abs center-line back-copy large" style="top:1743px">Activation time :10-60 min</div>
      <div class="abs center-line back-copy" style="top:1787px"><b>Warning :</b><br>For use by individuals 21 yrs of age or older or by registered<br>qualifying patients only. It is illegal to drive a motor vehicle while<br>under the influence of marijuana.</div>
      <div class="abs center-line back-copy large" style="top:1871px">Keep out of reach of children.</div>
      <div class="abs center-line back-copy large" style="top:1915px">Harborvale Safety Line Center<br>1 800 555 0147</div>
      <div class="abs back-copy pregnancy-box"><b>Warning :</b><br>Use by pregnant or breastfeeding women or by women who plan<br>to become pregnant may result in fetal injury, preterm birth,<br>low birthweight, or developmental problems for the child.</div>
      <div class="abs center-line back-copy" style="top:2077px">Made in a marijuana facility</div>
      <div class="abs center-line back-copy" style="top:2118px">Made &amp; distributed by Marlowe's Twig Company<br>License # BQ K 004736<br>(Logo)<br><span style="text-transform:none">www.FENWILLOWS.INFO</span></div>
    </section>
  </div>
</div>
</body>
</html>
```